Update Business Card Design

I'm looking to update my business cards. Attached is a photo of the current design. I like the black side so that does not have to be update. The white side needs to be updated. I want the design to be modern and minimalistic.
I am a lawyer and my firm's website is www.harborstonepartners.com (for reference).
My firm's logo has a horizontal version (which is on the black side of the card) and a vertical version (on the white side). I would prefer to keep the vertical version on the white side and horizontal version on the black side (the logo files are attached).

I am open to redesigning the black side also. I would like one side to have the horizontal logo and the other to have the vertical logo.

Went on vacation/holiday

```html
<!DOCTYPE html>
<html lang="en">
<head>
<meta charset="utf-8">
<title>Harborstone Partners – Business Card</title>
<link rel="stylesheet" href="https://fonts.googleapis.com/css2?family=Cinzel:wght@400;600&family=Merriweather:wght@400;700&display=swap">
<style>
  :root {
    --stage: #1f1f1f;
    --card-black: #141414;
    --card-white: #ffffff;
    --brand-blue: #00b3e3;
    --ink: #3a3a3a;
    --ink-soft: #555555;
    --light: #f2f2f2;
  }
  * { box-sizing: border-box; margin: 0; padding: 0; }
  html, body { width: 1200px; height: 1200px; overflow: hidden; }
  body {
    background: var(--stage);
    display: flex;
    flex-direction: column;
    align-items: center;
    justify-content: center;
    gap: 60px;
    font-family: "Merriweather", Georgia, serif;
  }
  .card {
    position: relative;
    width: 860px;
    height: 491px;
    overflow: hidden;
  }

  /* Front: black side */
  .card--front {
    background: var(--card-black);
    display: flex;
    flex-direction: column;
    align-items: center;
    justify-content: center;
    gap: 40px;
  }
  .wordmark {
    font-family: "Cinzel", Georgia, serif;
    font-weight: 600;
    color: var(--brand-blue);
    letter-spacing: 0.04em;
    line-height: 1.1;
  }
  .card--front .wordmark { font-size: 50px; text-align: center; }
  .website {
    font-family: "Cinzel", Georgia, serif;
    color: var(--light);
    font-size: 20px;
    letter-spacing: 0.18em;
    text-transform: uppercase;
  }

  /* Back: white side */
  .card--back { background: var(--card-white); color: var(--ink); }
  .card--back .wordmark {
    position: absolute;
    left: 56px;
    top: 60px;
    font-size: 42px;
  }
  .attorney {
    position: absolute;
    right: 56px;
    top: 140px;
    text-align: right;
  }
  .attorney__name {
    font-weight: 700;
    font-size: 26px;
    letter-spacing: 0.06em;
    text-transform: uppercase;
    color: var(--ink);
  }
  .attorney__title {
    font-size: 17px;
    color: var(--brand-blue);
    letter-spacing: 0.06em;
    margin-top: 4px;
  }
  .email {
    position: absolute;
    left: 56px;
    top: 236px;
    font-size: 16px;
    color: var(--ink-soft);
  }
  .divider {
    position: absolute;
    left: 40px;
    right: 40px;
    top: 272px;
    height: 2px;
    background: var(--brand-blue);
  }
  .phones {
    position: absolute;
    left: 56px;
    top: 300px;
    list-style: none;
    display: flex;
    flex-direction: column;
    gap: 10px;
  }
  .phones li {
    display: flex;
    align-items: center;
    gap: 14px;
    font-size: 18px;
    color: var(--ink-soft);
  }
  .phones svg { width: 24px; height: 24px; flex: none; }
  .address {
    position: absolute;
    right: 56px;
    top: 312px;
    text-align: right;
    font-style: normal;
    font-size: 18px;
    line-height: 1.55;
    color: var(--ink-soft);
  }
  .band {
    position: absolute;
    left: 0;
    right: 0;
    bottom: 0;
    height: 16px;
    background: var(--brand-blue);
  }
</style>
</head>
<body>

  <section class="card card--front" aria-label="Card front">
    <div class="wordmark">Harborstone Partners</div>
    <div class="website">www.harborstonepartners.com</div>
  </section>

  <section class="card card--back" aria-label="Card back">
    <div class="wordmark">Harborstone Partners</div>

    <div class="attorney">
      <div class="attorney__name">Daniel Okafor</div>
      <div class="attorney__title">Attorney at Law</div>
    </div>

    <div class="email">daniel@harborstonepartners.com</div>
    <div class="divider"></div>

    <ul class="phones">
      <li>
        <svg viewBox="0 0 24 24" aria-label="Mobile">
          <circle cx="12" cy="12" r="12" fill="var(--brand-blue)"/>
          <rect x="8" y="5" width="8" height="14" rx="1.5" fill="none" stroke="#fff" stroke-width="1.6"/>
          <circle cx="12" cy="16.5" r="0.9" fill="#fff"/>
        </svg>
        310.555.0142
      </li>
      <li>
        <svg viewBox="0 0 24 24" aria-label="Office phone">
          <circle cx="12" cy="12" r="12" fill="var(--brand-blue)"/>
          <path d="M5.5 10.5 Q12 5 18.5 10.5 L17 12 L15 11 L15 9.5 Q12 8.5 9 9.5 L9 11 L7 12 Z" fill="#fff"/>
          <rect x="8" y="12.5" width="8" height="5" rx="1" fill="#fff"/>
        </svg>
        310.555.0187
      </li>
      <li>
        <svg viewBox="0 0 24 24" aria-label="Fax">
          <circle cx="12" cy="12" r="12" fill="var(--brand-blue)"/>
          <rect x="8.5" y="5.5" width="7" height="4" fill="#fff"/>
          <rect x="6" y="10" width="12" height="6" rx="1" fill="#fff"/>
          <rect x="8.5" y="15" width="7" height="4" fill="#fff" stroke="var(--brand-blue)" stroke-width="0.8"/>
        </svg>
        310.555.0163
      </li>
    </ul>

    <address class="address">
      1180 Crescent Park Drive<br>
      Suite 312<br>
      Westbrook, CA 90417
    </address>

    <div class="band"></div>
  </section>

</body>
</html>
```